Business Card Design for a Lending Business (Hard Money loans)

We need a business card for our Real Estate Lending business. We do hard Money loans for real estate investors. We have an existing logo we like, see attached. I'd like the business card to mostly include the logo colors, but a bright color pop of some sort would be nice to see also. Card should include Logo, Company Name, Company Address, Employee Name, Cell Phone, Main Phone, Email, Website

Industry/Entity Type

Finance / Lending

Contact Information for Business Card

Logo, Company Name, Company Address, Employee Name, Cell Phone, Main Phone, Email, Website

Requirements
Nice to have
• I'd like the business card to mostly include the logo colors, but a bright color pop of some sort would be nice to see also.

```html
<!DOCTYPE html>
<html lang="en">
<head>
<meta charset="utf-8">
<title>Crestline Lending – Business Card</title>
<link href="https://fonts.googleapis.com/css2?family=Exo+2:wght@400;500;600&display=swap" rel="stylesheet">
<style>
  :root {
    --backdrop: #1f1f1f;
    --card-blue: #1a3cc0;
    --card-blue-deep: #0f2c9e;
    --accent-cyan: #1aa9e2;
    --text-white: #ffffff;
    --faint-mark: rgba(255, 255, 255, 0.06);
  }
  * { box-sizing: border-box; margin: 0; padding: 0; }
  html, body { width: 1200px; height: 939px; overflow: hidden; }
  body {
    background: var(--backdrop);
    font-family: "Exo 2", sans-serif;
    position: relative;
  }
  .card {
    position: absolute;
    width: 560px;
    height: 320px;
    border-radius: 22px;
    background: linear-gradient(135deg, var(--card-blue) 0%, var(--card-blue-deep) 100%);
    overflow: hidden;
  }
  .card-front { left: 110px; top: 90px; }
  .card-back { left: 530px; top: 520px; }

  .front-wordmark {
    position: absolute;
    inset: 0;
    display: flex;
    align-items: center;
    justify-content: center;
    gap: 18px;
  }
  .front-wordmark .mark-dot {
    width: 30px; height: 30px;
    border-radius: 50%;
    background: var(--accent-cyan);
  }
  .front-wordmark .company-name {
    color: var(--text-white);
    font-weight: 600;
    font-size: 40px;
    letter-spacing: 4px;
    text-transform: uppercase;
  }

  .back-decoration {
    position: absolute;
    left: -60px; top: 40px;
    width: 300px; height: 300px;
    border-radius: 50%;
    background: var(--faint-mark);
  }
  .person {
    position: absolute;
    right: 310px;
    top: 128px;
    text-align: right;
  }
  .person .person-name {
    color: var(--accent-cyan);
    font-weight: 600;
    font-size: 27px;
    text-transform: uppercase;
    letter-spacing: 0.5px;
    line-height: 1.1;
  }
  .person .person-role {
    color: var(--text-white);
    font-size: 18px;
    margin-top: 2px;
  }
  .divider {
    position: absolute;
    left: 270px; top: 70px;
    width: 1px; height: 180px;
    background: var(--accent-cyan);
  }
  .contact-list {
    position: absolute;
    left: 292px; top: 78px;
    list-style: none;
    color: var(--text-white);
    font-size: 14.5px;
    line-height: 1.35;
  }
  .contact-list li {
    display: flex;
    align-items: flex-start;
    gap: 10px;
    margin-bottom: 4px;
  }
  .contact-list svg {
    flex: none;
    width: 12px; height: 12px;
    margin-top: 4px;
    fill: var(--accent-cyan);
  }
  .contact-list .address { margin-bottom: 10px; }
</style>
</head>
<body>
  <section class="card card-front">
    <div class="front-wordmark">
      <span class="mark-dot"></span>
      <span class="company-name">Crestline Lending</span>
    </div>
  </section>

  <section class="card card-back">
    <div class="back-decoration"></div>
    <div class="person">
      <p class="person-name">Daniel Reyes</p>
      <p class="person-role">Founder &amp; CEO</p>
    </div>
    <div class="divider"></div>
    <ul class="contact-list">
      <li class="address">
        <svg viewBox="0 0 12 12"><path d="M6 0a4 4 0 0 0-4 4c0 3 4 8 4 8s4-5 4-8a4 4 0 0 0-4-4zm0 5.6A1.6 1.6 0 1 1 6 2.4a1.6 1.6 0 0 1 0 3.2z"/></svg>
        <span>Your Address, City, State<br>Country, Zip Code 1235</span>
      </li>
      <li>
        <svg viewBox="0 0 12 12"><path d="M2.4 0.5l2 2.2-1 1.3c.7 1.6 2 2.9 3.6 3.6l1.3-1 2.2 2-1 2.4C4.6 10.6 1.4 7.4.5 2.5z"/></svg>
        <span>(555) 201-4410</span>
      </li>
      <li>
        <svg viewBox="0 0 12 12"><path d="M3 0h6a1 1 0 0 1 1 1v10a1 1 0 0 1-1 1H3a1 1 0 0 1-1-1V1a1 1 0 0 1 1-1zm.6 1.2v8h4.8v-8zM6 9.8a.6.6 0 1 0 0 1.2.6.6 0 0 0 0-1.2z"/></svg>
        <span>(555) 201-4411</span>
      </li>
      <li>
        <svg viewBox="0 0 12 12"><path d="M3 0h6v3H3zM1 4h10a1 1 0 0 1 1 1v4h-2v3H2V9H0V5a1 1 0 0 1 1-1zm2.2 4.6v2.2h5.6V8.6z"/></svg>
        <span>(555) 201-4412</span>
      </li>
      <li>
        <svg viewBox="0 0 12 12"><path d="M0 2h12v1L6 7 0 3zm0 2.4l6 4 6-4V10H0z"/></svg>
        <span>hello@crestlinelending.com</span>
      </li>
      <li>
        <svg viewBox="0 0 12 12"><path d="M6 0a6 6 0 1 0 0 12A6 6 0 0 0 6 0zm0 1.2c.8 0 1.6 1.7 1.8 4.2H4.2C4.4 2.9 5.2 1.2 6 1.2zM4.2 6.6h3.6C7.6 9.1 6.8 10.8 6 10.8S4.4 9.1 4.2 6.6zM1.2 5.4A4.8 4.8 0 0 1 3.6 1.8 9 9 0 0 0 3 5.4zm0 1.2H3a9 9 0 0 0 .6 3.6 4.8 4.8 0 0 1-2.4-3.6zm7.8 0h1.8a4.8 4.8 0 0 1-2.4 3.6 9 9 0 0 0 .6-3.6zm0-1.2a9 9 0 0 0-.6-3.6 4.8 4.8 0 0 1 2.4 3.6z"/></svg>
        <span>www.crestlinelending.com</span>
      </li>
    </ul>
  </section>
</body>
</html>
```